R.T. Marlowe Electrical work flyer

I need a flyer design to help generate some extra work. I'm more than happy for a designer to play around with pictures, text, headings, boarders. The flyer will be double sided A4 size.
We specialize in Residential, Commercial, & Industrial Electrical works including PV Solar System Designs & Installations, Maintenance, System Checks & Upgrades, Mains Upgrades, Overhead & Underground, Switchboard Installations & Upgrades, Safety Switches, Spa & Pool connections, LED Lighting solutions, Energy Audit Checks, Fans & Air Conditioning, Hi-bay Lighting, Carpark Lighting, Data Points, Comms Racks, New Home Builds, Office Fitouts ...
We pride ourselves on always doing a great job, guaranteed workmanship, competitive pricing, & leaving the site clean.
Call Derek for a quote on any of your electrical needs
Mobile:0417 386 204
Email: rtmarloweelectrical@vendamail.example
PO Box 58
Brindle Vale VIC 3194

REC: 38071
CEC Accreditation: A3182096

I've added my company logo & some pics, photo's & electrical / solar brand logos that can be used but not a must. I'm more than happy if you can find better pics.

Target Market(s)

Office, Factory & Home Owners

Industry/Entity Type

Electrical

Font styles to use
Serif
Sans Serif

Requirements
Must have
• eye catchy design with not to much information overload.
• Just aiming for people to call up for quotes etc.
Nice to have
• My company logo, electrical & solar works available
Should not have
• pictures of kids

```html
<!DOCTYPE html>
<html lang="en">
<head>
<meta charset="utf-8">
<title>R.T. Marlowe Electrical – Flyer</title>
<link rel="stylesheet" href="https://fonts.googleapis.com/css2?family=Open+Sans:wght@400;600;700;800&family=Oswald:wght@500;700&display=swap">
<style>
  :root {
    --green: #5cb82e;
    --green-dark: #3e8e1c;
    --green-light: #8fd84f;
    --blue-deep: #04263f;
    --blue-mid: #0d5d86;
    --blue-light: #3ab0d8;
    --ink: #4a4a4a;
    --ink-dark: #222;
    --red: #d62020;
    --white: #ffffff;
  }
  * { box-sizing: border-box; margin: 0; padding: 0; }
  html, body { width: 900px; height: 1200px; overflow: hidden; background: #fff; }
  body { font-family: "Open Sans", Arial, sans-serif; color: var(--ink); }
  .flyer { position: relative; width: 900px; height: 1200px; background: var(--white); overflow: hidden; }
  .backdrop { position: absolute; inset: 0; }

  .photo-circle {
    position: absolute; border-radius: 50%;
    border: 6px solid var(--white);
    box-shadow: 0 4px 12px rgba(0,0,0,.3);
  }
  .photo-solar { left: 170px; top: 260px; width: 250px; height: 250px;
    background: radial-gradient(circle at 40% 35%, #9fc8e8, #4d7ea8 55%, #2a3d55); }
  .photo-carpark { left: 220px; top: 460px; width: 200px; height: 200px;
    background: radial-gradient(circle at 50% 40%, #3c5c8c, #142540 70%); }

  .pricing-stamp {
    position: absolute; left: 40px; top: 540px;
    transform: rotate(-12deg);
    border: 4px solid var(--red); color: var(--red);
    font-family: "Oswald", Impact, sans-serif; font-weight: 700;
    font-size: 26px; line-height: 1; text-align: center;
    padding: 6px 10px; letter-spacing: 1px;
  }

  .brand { position: absolute; left: 40px; top: 670px; display: flex; align-items: center; gap: 14px; }
  .brand-dot { width: 56px; height: 56px; border-radius: 50%; background: var(--green); }
  .brand-name { font-size: 40px; font-weight: 400; color: var(--ink); letter-spacing: -.5px; white-space: nowrap; }

  .services { position: absolute; left: 40px; top: 752px; width: 450px; }
  .services-title {
    background: var(--green); color: var(--white);
    font-size: 22px; font-weight: 700; padding: 4px 16px; margin-bottom: 8px;
  }
  .services-list { list-style: none; padding-left: 14px; }
  .services-list li {
    font-size: 14px; font-weight: 700; color: var(--ink-dark);
    line-height: 18px; display: flex; align-items: center; gap: 8px;
  }
  .services-list svg { flex: none; }

  .call-box {
    position: absolute; left: 520px; top: 752px; width: 340px;
    border-radius: 14px; border: 3px solid var(--green);
    background: var(--white); text-align: center; overflow: hidden;
  }
  .call-head {
    background: linear-gradient(180deg, var(--green-light), var(--green));
    color: var(--white); padding: 20px 0 14px;
  }
  .call-title { font-size: 46px; font-weight: 800; line-height: 1; letter-spacing: .5px; }
  .call-sub { font-size: 15px; font-weight: 600; margin-top: 10px; }
  .call-band {
    background: var(--green-dark); color: var(--white);
    font-size: 20px; font-weight: 800; padding: 10px 0;
  }
  .phone {
    padding: 22px 0 24px;
    font-size: 46px; font-weight: 800; color: var(--ink-dark);
    letter-spacing: .5px; line-height: 1; white-space: nowrap;
  }

  .footer {
    position: absolute; left: 0; bottom: 0; width: 900px; height: 52px;
    background: var(--green); color: var(--white);
    display: flex; align-items: center; justify-content: space-between;
    padding: 0 40px; font-size: 16px; font-weight: 600;
  }
  .footer-ids span + span::before { content: "|"; margin: 0 14px; }
</style>
</head>
<body>
<div class="flyer">
  <svg class="backdrop" width="900" height="1200" viewBox="0 0 900 1200">
    <defs>
      <radialGradient id="bulbGlow" cx="0.6" cy="0.45" r="0.7">
        <stop offset="0" stop-color="#5cc6ea"/>
        <stop offset="0.45" stop-color="#0d5d86"/>
        <stop offset="1" stop-color="#04263f"/>
      </radialGradient>
    </defs>
    <g role="img" aria-label="Photo of hanging light bulbs, including an LED bulb, against a blue background">
      <path d="M0 0 H900 V560 C720 520 560 470 420 380 C300 300 180 260 0 250 Z" fill="url(#bulbGlow)"/>
    </g>
    <path d="M0 250 C180 260 300 300 420 380 C560 470 720 520 900 560 V610 C700 590 520 520 400 440 C280 360 170 330 0 320 Z" fill="var(--green)"/>
    <path d="M0 320 C170 330 280 360 400 440 C520 520 700 590 900 610 V630 C690 620 510 550 390 470 C270 390 160 360 0 350 Z" fill="var(--green-light)" opacity=".7"/>
    <path d="M30 230 L120 170 L105 210 C150 215 190 225 220 240 C170 235 120 235 80 245 L95 270 Z" fill="var(--white)"/>
  </svg>

  <div class="photo-circle photo-solar" role="img" aria-label="Photo of solar panels on a rooftop"></div>
  <div class="photo-circle photo-carpark" role="img" aria-label="Photo of carpark lighting at night"></div>

  <div class="pricing-stamp">COMPETITIVE<br>PRICING</div>

  <div class="brand">
    <div class="brand-dot"></div>
    <div class="brand-name">R.T. Marlowe Electrical</div>
  </div>

  <section class="services">
    <h2 class="services-title">We specialize in</h2>
    <ul class="services-list">
      <li><svg width="12" height="12" viewBox="0 0 12 12"><path d="M1 6 L5 10 L11 2" stroke="#5cb82e" stroke-width="2.5" fill="none"/></svg>Residential</li>
      <li><svg width="12" height="12" viewBox="0 0 12 12"><path d="M1 6 L5 10 L11 2" stroke="#5cb82e" stroke-width="2.5" fill="none"/></svg>Commercial</li>
      <li><svg width="12" height="12" viewBox="0 0 12 12"><path d="M1 6 L5 10 L11 2" stroke="#5cb82e" stroke-width="2.5" fill="none"/></svg>Industrial Electrical works incl. PV Solar Designs &amp; Installations</li>
      <li><svg width="12" height="12" viewBox="0 0 12 12"><path d="M1 6 L5 10 L11 2" stroke="#5cb82e" stroke-width="2.5" fill="none"/></svg>Maintenance</li>
      <li><svg width="12" height="12" viewBox="0 0 12 12"><path d="M1 6 L5 10 L11 2" stroke="#5cb82e" stroke-width="2.5" fill="none"/></svg>System Checks &amp; Upgrades</li>
      <li><svg width="12" height="12" viewBox="0 0 12 12"><path d="M1 6 L5 10 L11 2" stroke="#5cb82e" stroke-width="2.5" fill="none"/></svg>Mains Upgrades</li>
      <li><svg width="12" height="12" viewBox="0 0 12 12"><path d="M1 6 L5 10 L11 2" stroke="#5cb82e" stroke-width="2.5" fill="none"/></svg>Overhead &amp; Underground</li>
      <li><svg width="12" height="12" viewBox="0 0 12 12"><path d="M1 6 L5 10 L11 2" stroke="#5cb82e" stroke-width="2.5" fill="none"/></svg>Switchboard Installations &amp; Upgrades</li>
      <li><svg width="12" height="12" viewBox="0 0 12 12"><path d="M1 6 L5 10 L11 2" stroke="#5cb82e" stroke-width="2.5" fill="none"/></svg>Safety Switches</li>
      <li><svg width="12" height="12" viewBox="0 0 12 12"><path d="M1 6 L5 10 L11 2" stroke="#5cb82e" stroke-width="2.5" fill="none"/></svg>Spa &amp; Pool connections</li>
      <li><svg width="12" height="12" viewBox="0 0 12 12"><path d="M1 6 L5 10 L11 2" stroke="#5cb82e" stroke-width="2.5" fill="none"/></svg>LED Lighting solutions</li>
      <li><svg width="12" height="12" viewBox="0 0 12 12"><path d="M1 6 L5 10 L11 2" stroke="#5cb82e" stroke-width="2.5" fill="none"/></svg>Energy Audit Checks</li>
      <li><svg width="12" height="12" viewBox="0 0 12 12"><path d="M1 6 L5 10 L11 2" stroke="#5cb82e" stroke-width="2.5" fill="none"/></svg>Fans &amp; Air Conditioning</li>
      <li><svg width="12" height="12" viewBox="0 0 12 12"><path d="M1 6 L5 10 L11 2" stroke="#5cb82e" stroke-width="2.5" fill="none"/></svg>Hi-bay Lighting, Carpark Lighting</li>
      <li><svg width="12" height="12" viewBox="0 0 12 12"><path d="M1 6 L5 10 L11 2" stroke="#5cb82e" stroke-width="2.5" fill="none"/></svg>Data Points,</li>
      <li><svg width="12" height="12" viewBox="0 0 12 12"><path d="M1 6 L5 10 L11 2" stroke="#5cb82e" stroke-width="2.5" fill="none"/></svg>Comms Racks,</li>
      <li><svg width="12" height="12" viewBox="0 0 12 12"><path d="M1 6 L5 10 L11 2" stroke="#5cb82e" stroke-width="2.5" fill="none"/></svg>New Home Builds,</li>
      <li><svg width="12" height="12" viewBox="0 0 12 12"><path d="M1 6 L5 10 L11 2" stroke="#5cb82e" stroke-width="2.5" fill="none"/></svg>Office Fitouts ...</li>
    </ul>
  </section>

  <div class="call-box">
    <div class="call-head">
      <div class="call-title">CALL DEREK</div>
      <div class="call-sub">FOR A QUOTE ON ANY OF</div>
    </div>
    <div class="call-band">YOUR ELECTRICAL NEEDS</div>
    <div class="phone">0417 386 204</div>
  </div>

  <footer class="footer">
    <span class="footer-web">www.rtmarlowe-electrical.example</span>
    <span class="footer-ids"><span>REC: 38071</span><span>CEC Accreditation: A3182096</span></span>
  </footer>
</div>
</body>
</html>
```